Flyer for Children Therapy Center

We need a flyer with front and back with the following services:

Services:
- Fisioterapia (File 3: B.jpg)
- Terapia Ocupacional (G.jpg)
- Terapia da Fala (H.jpg)
- Musicoterapia (File 4: C.jpg)
- Estimulação Elétrica Neurofuncional (File 2: molli.jpg)
- Entre outros!

Products:
- Fitoterapia Tradicional Chinesa (I.jpg)
- Ortóteses dinâmicas funcionais (Before: E.1.jpg, After: E.2.jpg)
- Fato de compressão dinâmica sob medida (Before: F.1.jpg, After: F.2.jpg)
- Assento pélvico moldado com técnica exclusiva (File 5: D.jpg)

Target Market(s)

Parents of children with special needs

Colors

Designer to choose colors to be used in the design.

Requirements
Must have
• The flyer must have:
• - Our logo
• - Company Name: Brota Num Abraço
• - center description: Centro de Terapias Especializadas para crianças e jovens.
• - Slogan: Semeamos amor, colhemos sorrisos, distribuímos vitórias!
• - Site: www.vinhal.pt
• - Facebook: www.facebook.com/brotanumabraco
• - Cellular phone: +351 917 458 302
• - Land Line: +351 219 640 527
• - E-mail: geral@vinhal.pt
• - Address: R. Fernando Lemos Queirós 4B, 2617-581 - Vale do Ribeirinho, Portugal
Nice to have
• Logo colors
Should not have
• Dark colors.

```html
<!DOCTYPE html>
<html lang="pt">
<head>
<meta charset="utf-8">
<title>Brota Num Abraço – Flyer</title>
<link href="https://fonts.googleapis.com/css2?family=Oswald:wght@600;700&family=Roboto+Condensed:wght@700&family=Roboto:wght@500;700&family=Lato:wght@400;700;900&display=swap" rel="stylesheet">
<style>
:root{
  --red:#e5473f;
  --teal:#2aa596;
  --white:#ffffff;
  --ink:#2b2b2b;
  --muted:#6e6e6e;
  --bg:#e9e9e9;
  --paper:#fbfbfb;
  --badge:#e6e6e6;
}
*{box-sizing:border-box;margin:0;padding:0}
html,body{width:1200px;height:1200px;overflow:hidden;background:var(--bg)}
body{position:relative;font-family:"Lato",sans-serif;color:var(--ink)}
.flyer{position:absolute;top:204px;width:560px;height:792px;background:var(--paper);overflow:hidden;box-shadow:0 2px 10px rgba(0,0,0,.18)}
.flyer--front{left:25px}
.flyer--back{left:615px}
.photo{position:absolute;left:0;width:100%}
.abs{position:absolute}

/* front */
.front-photo{top:0;height:253px;background:linear-gradient(100deg,#f4ecd9 0%,#eadfc6 35%,#d9b48e 60%,#6d9bcf 85%,#3d79bd 100%)}
.teal-rule{left:0;top:253px;width:100%;height:6px;background:var(--teal)}
.hero-band{left:0;top:259px;width:100%;height:154px;background:var(--red)}
.hero-divider{left:307px;top:259px;width:3px;height:154px;background:rgba(255,255,255,.35)}
.slogan{left:24px;top:284px;font-family:"Oswald",sans-serif;font-weight:700;color:var(--white);letter-spacing:.2px}
.slogan span{display:block;line-height:1.2}
.slogan .l1{font-size:30px}
.slogan .l2{font-size:25px}
.slogan .l3{font-size:23px}
.brand-block{left:323px;top:286px;color:var(--white);font-family:"Roboto Condensed",sans-serif;font-weight:700}
.brand-block .big{font-size:54px;line-height:1;letter-spacing:1px}
.brand-block .small{font-family:"Roboto",sans-serif;font-weight:500;font-size:28px;margin-top:8px;letter-spacing:.5px}

.tab{position:absolute;height:24px;background:var(--teal);color:var(--white);font-family:"Roboto",sans-serif;font-weight:500;font-size:16px;line-height:24px}
.tab--services{left:0;top:406px;width:128px;padding-left:26px;clip-path:polygon(0 0,100% 0,93% 100%,0 100%)}
.services-rule{left:120px;top:425px;width:440px;height:5px;background:var(--teal)}

.svc{position:absolute;width:120px;text-align:center;font-size:10px;color:var(--ink)}
.svc .disc{display:block;width:74px;height:74px;margin:0 auto 6px;border-radius:50%;border:2px solid var(--red)}
.c1{background:linear-gradient(135deg,#f2b340,#4bb0d8 55%,#d84b7a)}
.c2{background:linear-gradient(135deg,#f0c3a0,#e25d3a 50%,#3a8fd1)}
.c3{background:linear-gradient(135deg,#c89a84,#6b3c33 50%,#e36d4a)}
.c4{background:linear-gradient(135deg,#f4efe6,#e4c69a 50%,#8a6b55)}
.c5{background:linear-gradient(135deg,#e8f0f3,#3ea8a0 50%,#4a3f3c)}
.c6{background:linear-gradient(135deg,#f6e9c8,#e36c4c 50%,#4c93cf)}

.center-desc{right:26px;top:440px;text-align:right;font-family:"Roboto",sans-serif;font-weight:700;font-size:21px;line-height:1.22}
.center-desc .red{color:var(--red)}
.center-desc .teal{color:var(--teal)}
.tab--about{right:0;top:536px;width:130px;text-align:center;padding-left:10px;clip-path:polygon(6% 0,100% 0,100% 100%,0 100%)}
.about-text{left:276px;top:574px;width:260px;font-size:11.2px;line-height:1.3;text-align:justify;text-align-last:right;color:var(--ink)}
.wordmark{left:330px;top:670px;display:flex;align-items:center;gap:8px;font-family:"Roboto",sans-serif;font-weight:700;font-size:17px;color:var(--teal)}
.wordmark .dot{width:22px;height:22px;border-radius:50%;background:var(--red)}

.call{position:absolute;height:24px;background:var(--teal);color:var(--white);font-family:"Roboto",sans-serif;font-weight:500;font-size:15px;line-height:24px}
.call--front{left:280px;top:747px;width:280px;padding-left:28px;clip-path:polygon(4% 0,100% 0,100% 100%,0 100%)}
.foot{left:0;top:765px;width:100%;height:27px;background:var(--red)}
.foot-text{left:24px;top:768px;font-size:6.6px;line-height:1.5;color:var(--white)}

/* back */
.back-photo{top:0;height:294px;background:linear-gradient(180deg,#f1f1ee 0%,#e5e5e2 55%,#9ed66b 75%,#6a8fbf 100%)}
.title-band{left:0;top:301px;width:100%;height:116px;background:var(--teal);display:flex;align-items:center;justify-content:center;font-family:"Lato",sans-serif;font-weight:900;font-size:46px;color:var(--white);letter-spacing:.5px}
.tab--products{left:0;top:427px;width:124px;padding-left:24px;clip-path:polygon(0 0,100% 0,94% 100%,0 100%)}
.products-rule{left:118px;top:431px;width:442px;height:7px;background:var(--red)}
.prod{position:absolute;width:220px;text-align:center;font-family:"Lato",sans-serif;font-weight:700;font-size:11px;color:var(--ink)}
.prod .disc{display:block;width:116px;height:116px;margin:0 auto 10px;border-radius:50%;border:2px solid var(--red)}
.p-badge{background:var(--white);display:flex !important;align-items:center;justify-content:center}
.p-badge i{width:70px;height:70px;border-radius:50%;background:var(--badge)}
.p2{background:linear-gradient(180deg,#d8cfc4 0%,#b59a86 45%,#7bc1d2 75%,#f1b64a 100%)}
.p3{background:linear-gradient(90deg,#e6cfc0 0%,#c98a76 48%,#3a4f86 52%,#2b3c6e 100%)}
.p4{background:linear-gradient(90deg,#c9b6a6 0%,#4a6aa0 48%,#d8493f 55%,#c8b39c 100%)}
.call--back{left:0;top:752px;width:290px;padding-left:26px;clip-path:polygon(0 0,100% 0,96% 100%,0 100%)}
.foot--back{top:770px;height:22px}
.fb-text{right:70px;top:776px;font-size:7px;color:var(--white)}
</style>
</head>
<body>

<section class="flyer flyer--front">
  <div class="photo front-photo" role="img" aria-label="Therapist smiling at a young girl during a speech therapy session"></div>
  <div class="abs teal-rule"></div>
  <div class="abs hero-band"></div>
  <div class="abs hero-divider"></div>
  <h2 class="abs slogan"><span class="l1">SEMEAMOS AMOR</span><span class="l2">COLHEMOS SORRISOS</span><span class="l3">DISTRIBUÍMOS VITÓRIAS!</span></h2>
  <h1 class="abs brand-block"><div class="big">BROTA</div><div class="small">NUM ABRAÇO</div></h1>

  <div class="tab tab--services">SERVICES:</div>
  <div class="abs services-rule"></div>

  <div class="svc" style="left:42px;top:442px"><span class="disc c1" role="img" aria-label="Child in physiotherapy session"></span>Fisioterapia</div>
  <div class="svc" style="left:164px;top:440px"><span class="disc c2" role="img" aria-label="Child in occupational therapy"></span>Terapia Ocupacional</div>
  <div class="svc" style="left:42px;top:545px"><span class="disc c3" role="img" aria-label="Child playing music with therapist"></span>Musicoterapia</div>
  <div class="svc" style="left:164px;top:543px"><span class="disc c4" role="img" aria-label="Speech therapy session"></span>Terapia da Fala</div>
  <div class="svc" style="left:42px;top:650px;line-height:1.15"><span class="disc c5" role="img" aria-label="Child during electrical stimulation therapy"></span>Estimulação Elétrica<br>Neurofuncional</div>
  <div class="svc" style="left:164px;top:652px"><span class="disc c6" role="img" aria-label="Child in therapy suit exercising"></span>Entre outros!</div>

  <div class="abs center-desc"><div class="red">CENTRO DE TERAPIAS</div><div class="teal">ESPECIALIZADAS PARA</div><div class="red">CRIANÇAS E JOVENS</div></div>
  <div class="tab tab--about">ABOUT US</div>
  <p class="abs about-text">This is our Tomás, who has enchanted our days in such a special way! Work in co-therapy (physiotherapy + music therapy) working in a holistic way all aspects of development.</p>
  <div class="abs wordmark"><span class="dot"></span>Brota Num Abraço</div>

  <div class="abs foot"></div>
  <div class="call call--front">CALL TODAY- +351 917 458 302</div>
  <div class="abs foot-text">R. Fernando Lemos Queirós 4B, 2617-581 - Vale do Ribeirinho, Portugal<br>E-mail: geral@vinhal.pt // website- www.vinhal.pt</div>
</section>

<section class="flyer flyer--back">
  <div class="photo back-photo" role="img" aria-label="Two children in therapy suits sitting on a green mat in the therapy gym"></div>
  <h2 class="abs title-band">BROTA NUM ABRAÇO</h2>
  <div class="tab tab--products">PRODUCTS:</div>
  <div class="abs products-rule"></div>

  <div class="prod" style="left:50px;top:448px"><span class="disc p-badge" role="img" aria-label="Partner badge"><i></i></span>FITOTERAPIA TRADICIONAL</div>
  <div class="prod" style="left:290px;top:448px"><span class="disc p2" role="img" aria-label="Child's feet with dynamic orthoses"></span>ORTÓTESES DINÂMICAS FUNCIO-</div>
  <div class="prod" style="left:50px;top:601px"><span class="disc p3" role="img" aria-label="Before and after with dynamic compression suit"></span>FITOTERAPIA TRADICIONAL</div>
  <div class="prod" style="left:290px;top:601px"><span class="disc p4" role="img" aria-label="Before and after with functional orthoses"></span>ORTÓTESES DINÂMICAS FUNCIONAIS</div>

  <div class="abs foot foot--back"></div>
  <div class="call call--back">CALL TODAY- +351 219 640 527</div>
  <div class="abs fb-text">Facebook: www.facebook.com/brotanumabraco</div>
</section>

</body>
</html>
```